Design for online reviews widget

Attached is a wireframe of a widget we need designing to display reviews on websites from multiple sources. We need this provided at 3 different sizes including full screen, contained (like the wireframe) and mobile.
You have completely free rein on the styling.
The only elements that should remain untouched are the blue stars (https://www.filquarry.net/s/8vtmwp2291zq4h/kv%20stars.ai?dl=0) and powered by logo at the bottom.
Ignore the menu at the top of the wireframe, this is just from the website the widget will be placed on.
Businesses

```html
<!DOCTYPE html>
<html lang="en">
<head>
<meta charset="utf-8">
<title>Reviews Widget</title>
<link href="https://fonts.googleapis.com/css2?family=Poppins:wght@400;500;600;700&display=swap" rel="stylesheet">
<style>
:root{
  --brand-blue:#19b4ee;
  --brand-blue-deep:#10a8ea;
  --ink:#222;
  --body:#555;
  --muted:#666;
  --pill:#efefef;
  --badge:#f1f1f1;
  --rule:#d9d9d9;
  --white:#fff;
}
*{box-sizing:border-box;margin:0;padding:0}
html,body{width:870px;height:1200px;overflow:hidden;background:var(--white);font-family:"Poppins",sans-serif}
.widget{position:relative;width:870px;height:1200px}
.rating-marks{position:absolute;top:22px;left:378px;display:flex;gap:6px}
.rating-marks span{width:34px;height:34px;border-radius:50%;background:var(--brand-blue);border:2px solid #0b9bd6}
.filter{position:absolute;left:649px;top:23px;width:156px;height:33px;border-radius:17px;background:var(--pill);color:var(--muted);font-size:10px;display:flex;align-items:center;justify-content:space-between;padding:0 14px 0 19px}
.score-banner{position:absolute;left:64px;top:78px;width:741px;height:170px;border-radius:10px;background:radial-gradient(circle at 50% 45%,#1cbcf2,var(--brand-blue-deep));color:var(--white);text-align:center;display:flex;flex-direction:column;justify-content:center;font-weight:700;font-size:34px;line-height:42px}
.review{position:absolute;width:353px}
.review-head{display:flex;align-items:center;gap:14px;height:86px}
.source-badge{flex:none;width:86px;height:86px;border-radius:50%;background:var(--badge);display:flex;flex-direction:column;align-items:center;justify-content:center;gap:5px;font-size:13px;font-weight:600;color:var(--ink)}
.score-dot{width:36px;height:36px;border-radius:50%;background:#164e97}
.review-title{font-size:13px;font-weight:600;color:var(--ink);line-height:18px}
.review-body{margin-top:18px;font-size:10.5px;line-height:16.1px;color:var(--body);text-align:justify}
.review-meta{margin-top:14px;font-size:9.5px;color:var(--body)}
.review-meta b{font-weight:600;color:#444}
.review-date{display:flex;align-items:center;gap:5px;margin-top:13px;font-size:9px;color:var(--muted)}
.review-date i{width:9px;height:9px;border-radius:50%;background:#c4c4c4}
.divider{position:absolute;top:604px;height:1px;width:353px;background:var(--rule)}
.load-more{position:absolute;left:373px;top:968px;width:126px;height:38px;border-radius:19px;background:#22bcee;color:var(--white);font-size:11px;font-weight:600;display:flex;align-items:center;justify-content:center}
.footer-rule{position:absolute;left:64px;top:1086px;width:742px;height:1px;background:var(--rule)}
.powered{position:absolute;left:0;top:1110px;width:870px;text-align:center;color:#111}
.powered p{font-size:16px}
.powered .brand{display:inline-flex;align-items:center;gap:8px;font-size:24px;font-weight:700;margin-top:2px}
.powered .brand span{width:22px;height:22px;border-radius:50%;background:var(--brand-blue)}
</style>
</head>
<body>
<div class="widget">
  <div class="rating-marks" aria-label="Three rating marks"><span></span><span></span><span></span></div>
  <div class="filter">Filter results
    <svg width="8" height="6" viewBox="0 0 8 6"><path d="M1 1l3 3 3-3" fill="none" stroke="#333" stroke-width="1.4"/></svg>
  </div>
  <div class="score-banner"><div>Combined Review Score</div><div>2.3 out of 3</div></div>

  <article class="review" style="left:64px;top:321px">
    <div class="review-head">
      <div class="source-badge">TradeVouch<span class="score-dot"></span></div>
      <h3 class="review-title">Front door with windows each<br>side and side window</h3>
    </div>
    <p class="review-body">This is the second time we have used meridian home Improvments , and the service is amazing! Owen came round several times as we keep changing our minds and he was so helpful and gave us good advice, and the guys who do the fitting are efficient and tidy . I've got to say the end result is amazing and I have recommended to many of friends . Thanks Meridian</p>
    <p class="review-meta"><b>Reliablity:</b> 9.38 <b>Courtesy:</b> 10 <b>Tidiness:</b> 9.84 <b>Workmanship:</b> 10</p>
    <p class="review-date"><i></i>Verified 28th September 2021</p>
  </article>

  <article class="review" style="left:453px;top:321px">
    <div class="review-head">
      <div class="source-badge">Searchly</div>
      <h3 class="review-title">Positive: Professionalism,<br>Quality, Value</h3>
    </div>
    <p class="review-body">The team did a good job of replacing a large feature window spanning two floors, as well as the others in my property. They're a professional group who were willing to work out solutions to any problem, especially compared to other companies. Prices are fair, and my new UPVC windows look great. Special thanks to Frank for being so accommodating and for the good communication throughout.</p>
    <p class="review-meta"><b>Service:</b> Window installation</p>
    <p class="review-date"><i></i>11 months ago by Daniel Hurst</p>
  </article>

  <div class="divider" style="left:64px"></div>
  <div class="divider" style="left:453px"></div>

  <article class="review" style="left:64px;top:643px">
    <div class="review-head">
      <div class="source-badge">Listora</div>
      <h3 class="review-title">Brilliant all round professional,<br>friendly service.</h3>
    </div>
    <p class="review-body">This home run friendly business was a real pleasure to deal with. From the professional, no pressure quote, nothing was too much trouble to ensure everything is as required for your needs with the quote and fitting. The workmanship and double glazing being fitted was brilliant and my home/outdoors was left tidy and clean leaving an outstanding impression for such an all round professional job. I would not hesitate to recommend this company, such a brilliant service from great hardworking people that care about their service.</p>
    <p class="review-date"><i></i>13 Feb 2018 by GreenChair4</p>
  </article>

  <article class="review" style="left:453px;top:643px">
    <div class="review-head">
      <div class="source-badge">TrustBeacon</div>
      <h3 class="review-title">Front door with windows each side<br>and side window</h3>
    </div>
    <p class="review-body">This is the second time we have used meridian home Improvments , and the service is amazing! Owen came round several times as we keep changing our minds and he was so helpful and gave us good advice, and the guys who do the fitting are efficient and tidy . I've got to say the end result is amazing and I have recommended to many of friends . Thanks Meridian</p>
    <p class="review-date" style="margin-top:61px"><i></i>13 Feb 2018 by Tom</p>
  </article>

  <div class="load-more">LOAD MORE</div>
  <div class="footer-rule"></div>
  <div class="powered">
    <p>Powered by</p>
    <div class="brand"><span></span>ScoreWeave</div>
  </div>
</div>
</body>
</html>
```